Telecommunications/Power civil contractor needs business card design

Were a new telecommunications/power underground civil contractor that is looking for a new business card design. Our company colours are silver or grey and orange. Feel free to use the white background logo or the black background logo.

Target Market(s)

Local contractors, utility companies, private sector mining/energy companies, developers.

Industry/Entity Type

Telecommunications

Contact Information for Business Card

Each card will need the following info:
Persons name:
Title:
E-mail:
Phone number:
Shop Address:
Mailing Address:

Requirements
Must have
• Each card will need the following info:
• Persons name:
• Title:
• E-mail:
• Phone number:
• Shop Address:
• Mailing Address:

```html
<!DOCTYPE html>
<html lang="en">
<head>
<meta charset="utf-8">
<title>Ridgeline Contracting – Business Card</title>
<link href="https://fonts.googleapis.com/css2?family=Exo+2:wght@500;700;800&family=Roboto:wght@400&display=swap" rel="stylesheet">
<style>
  :root {
    --stage: #4a413c;
    --card: #141414;
    --card-edge: #0c0c0c;
    --orange: #f15a24;
    --silver: #9a9a9a;
    --silver-light: #c8c8c8;
    --text-soft: #d0d0d0;
  }
  * { box-sizing: border-box; margin: 0; padding: 0; }
  html, body {
    width: 1200px; height: 814px; overflow: hidden;
    background: var(--stage);
  }
  .stage {
    position: relative; width: 1200px; height: 814px;
    display: flex; align-items: center; justify-content: center; gap: 50px;
  }
  .card {
    position: relative; width: 525px; height: 300px;
    background: var(--card);
    box-shadow: 0 10px 28px rgba(0,0,0,.45);
    overflow: hidden;
  }
  /* front */
  .brand {
    position: absolute; left: 36px; top: 48px;
    display: flex; align-items: center; gap: 12px;
  }
  .brand-dot {
    width: 40px; height: 40px; border-radius: 50%;
    border: 3px solid var(--silver);
  }
  .brand-name {
    font-family: "Exo 2", sans-serif; font-weight: 800;
    font-size: 22px; letter-spacing: .5px; color: var(--orange);
    line-height: 1.05;
  }
  .person {
    position: absolute; left: 36px; top: 168px;
    font-family: "Exo 2", sans-serif;
  }
  .person-name {
    font-weight: 700; font-size: 21px; color: var(--orange); letter-spacing: .5px;
  }
  .person-title {
    font-weight: 500; font-size: 16px; color: var(--text-soft); margin-top: 2px;
  }
  .contact {
    position: absolute; left: 300px; top: 56px;
    font-family: "Roboto", sans-serif; font-size: 14px; color: var(--text-soft);
    line-height: 1.45;
  }
  .contact-address { margin-bottom: 4px; }
  .contact-row { display: flex; align-items: center; gap: 8px; }
  .contact-row svg { width: 13px; height: 13px; flex: none; }
  .band-orange {
    position: absolute; left: 0; bottom: 0; width: 290px; height: 34px;
    background: var(--orange);
  }
  .band-silver {
    position: absolute; left: 290px; bottom: 0; right: 0; height: 44px;
    background: linear-gradient(180deg, var(--silver-light), var(--silver) 60%, #6e6e6e);
  }
  .band-silver::after {
    content: ""; position: absolute; left: 0; right: 0; bottom: 0; height: 34px;
    background: var(--card-edge); opacity: 0;
  }
  /* back */
  .back-mark {
    position: absolute; right: 34px; top: 32px;
    display: flex; align-items: center; gap: 10px;
  }
  .back-dot {
    width: 44px; height: 44px; border-radius: 50%;
    border: 3px solid var(--silver);
  }
  .back-name {
    font-family: "Exo 2", sans-serif; font-weight: 800;
    font-size: 13px; color: var(--silver); letter-spacing: .5px;
  }
</style>
</head>
<body>
<main class="stage">
  <section class="card card-front">
    <div class="brand">
      <span class="brand-dot"></span>
      <span class="brand-name">RIDGELINE<br>CONTRACTING</span>
    </div>
    <div class="person">
      <p class="person-name">DANIEL REYES</p>
      <p class="person-title">CEO/ FOUNDER</p>
    </div>
    <div class="contact">
      <p class="contact-address">4120 Birchwood Road<br>Fairbanks, Alaska 99701</p>
      <p class="contact-row">
        <svg viewBox="0 0 16 16"><circle cx="8" cy="8" r="8" fill="#f15a24"/><path d="M5.2 4.2l1.4-.2.8 2-1 .8c.5 1.1 1.3 1.9 2.4 2.4l.8-1 2 .8-.2 1.4c-3.4.3-6.4-2.7-6.2-6.2z" fill="#141414"/></svg>
        555 214 7760
      </p>
      <p class="contact-row">
        <svg viewBox="0 0 16 16"><circle cx="8" cy="8" r="8" fill="#f15a24"/><rect x="4" y="5" width="8" height="6" fill="#141414"/><path d="M4 5l4 3.3L12 5" stroke="#f15a24" stroke-width="1" fill="none"/></svg>
        dan@ridgelinecivil.com
      </p>
      <p class="contact-row">
        <svg viewBox="0 0 16 16"><circle cx="8" cy="8" r="8" fill="#f15a24"/><circle cx="8" cy="8" r="4.3" fill="none" stroke="#141414" stroke-width="1.2"/><path d="M3.7 8h8.6M8 3.7c-2 2.4-2 6.2 0 8.6M8 3.7c2 2.4 2 6.2 0 8.6" stroke="#141414" stroke-width="1" fill="none"/></svg>
        www.ridgelinecivil.com
      </p>
    </div>
    <div class="band-orange"></div>
    <div class="band-silver"></div>
  </section>

  <section class="card card-back">
    <div class="back-mark">
      <span class="back-name">RIDGELINE CONTRACTING</span>
      <span class="back-dot"></span>
    </div>
  </section>
</main>
</body>
</html>
```